Riverline Estate Holdings Co.

We need a logo and business card design for a Hong Kong based real estate company, KDT Land. We are want the brand to reflect the owners forward thinking, creative, and trend setting projects, while also reflecting a sense of security and strength. We invest in industrial properties which we convert to co-living or co-working spaces. KDT stands for Greater Bay Area which is the region around southern China including HK, Macau, and 9 other Chinese cities...made up of approx. 68 million people. There are massive infrastructure projects including the bridge to Macau and high-speed rail to SZ and the bridge connecting SZ and Zhongshan.

Target Market(s)

Chinese and western retail investors, as well as institutional investors

Industry/Entity Type

Real Estate Development

Contact Information for Business Card

Owen Tallis
CEO
owen@kdtland-hq.com
M + 852 9416 2057
F + 852 3582 0400
Suite 2207, The Meridale, 41 Larchmont Rd., Central, Hong Kong

Logo Text

kdt land (company name) lifestyle property development (underneath)

Colors

Designer to choose colors to be used in the design.

Requirements
Must have
• Details listed above. One side should include the logo and company name...kdt land in modern, hip styling with "lifestyle property development"
Nice to have
• Could be a Black card, with metallic purple "kdt" and white "land"...but open great design ideas
Should not have
• boring and traditional layout

```html
<!DOCTYPE html>
<html lang="en">
<head>
<meta charset="utf-8">
<title>KDT Land — Business Card</title>
<link rel="stylesheet" href="https://fonts.googleapis.com/css2?family=Oswald:wght@500;600&family=Open+Sans:wght@400;600&display=swap">
<style>
  :root {
    --backdrop: #9a9a9a;
    --card-dark: #242122;
    --purple: #a12bb5;
    --purple-bright: #b52fc6;
    --purple-deep: #8a1491;
    --white: #ffffff;
    --text-light: #e9e6e8;
  }
  * { margin: 0; padding: 0; box-sizing: border-box; }
  html, body {
    width: 1200px; height: 900px; overflow: hidden;
    background: var(--backdrop);
  }
  .canvas { position: relative; width: 1200px; height: 900px; }

  .card { position: absolute; top: 200px; width: 310px; height: 503px; }

  .card-front {
    left: 253px;
    background: var(--card-dark);
    border-radius: 52px 0 52px 0;
  }
  .card-back {
    left: 627px;
    border-radius: 0 48px 0 48px;
    background: radial-gradient(ellipse at 45% 30%, var(--purple-bright) 0%, var(--purple) 45%, var(--purple-deep) 100%);
  }

  .wordmark {
    position: absolute;
    font-family: 'Oswald', sans-serif;
    font-weight: 600;
    letter-spacing: 1px;
    line-height: 1;
    white-space: nowrap;
  }
  .card-front .wordmark { left: 44px; top: 108px; font-size: 58px; color: var(--purple); }
  .card-back .wordmark { left: 42px; top: 204px; font-size: 60px; color: var(--white); }

  .tagline {
    position: absolute; left: 0; right: 0; top: 312px;
    text-align: center;
    font-family: 'Oswald', sans-serif;
    font-weight: 500;
    font-size: 17px;
    line-height: 23px;
    letter-spacing: 0.4px;
    color: var(--white);
  }

  .person { position: absolute; left: 33px; top: 287px; }
  .person-name {
    font-family: 'Oswald', sans-serif; font-weight: 500;
    font-size: 20px; line-height: 24px; color: var(--purple-bright);
  }
  .person-title {
    font-family: 'Open Sans', sans-serif; font-size: 14px; line-height: 18px; color: var(--text-light);
  }

  .contact-list { position: absolute; left: 33px; top: 343px; list-style: none; }
  .contact-list li {
    display: flex; align-items: center; gap: 4px;
    font-family: 'Open Sans', sans-serif; font-size: 14.5px; line-height: 18px; color: var(--text-light);
  }
  .contact-list svg { width: 11px; height: 11px; fill: var(--purple-bright); flex: none; }

  .address {
    position: absolute; left: 30px; top: 410px;
    font-family: 'Open Sans', sans-serif; font-style: normal;
    font-size: 14.5px; line-height: 18px; color: var(--text-light);
  }
</style>
</head>
<body>
<main class="canvas">
  <section class="card card-front" aria-label="Card front">
    <div class="wordmark">KDT LAND</div>
    <div class="person">
      <p class="person-name">OWEN TALLIS</p>
      <p class="person-title">CEO</p>
    </div>
    <ul class="contact-list">
      <li>
        <svg viewBox="0 0 12 12" aria-label="Mobile"><path d="M3 0h6a1 1 0 0 1 1 1v10a1 1 0 0 1-1 1H3a1 1 0 0 1-1-1V1a1 1 0 0 1 1-1zm.5 1.5v8h5v-8z"/></svg>
        + 852 9416 2057
      </li>
      <li>
        <svg viewBox="0 0 12 12" aria-label="Fax"><path d="M3 0h6v3H3zM0 4h12v5h-2V7H2v2H0zM3 8h6v4H3z"/></svg>
        + 852 3582 0400
      </li>
      <li>
        <svg viewBox="0 0 12 12" aria-label="Email"><path d="M0 2h12v1L6 7 0 3zM0 4.5l6 4 6-4V10H0z"/></svg>
        owen@kdtland-hq.com
      </li>
    </ul>
    <address class="address">
      Suite 2207, The Meridale<br>
      41 Larchmont Rd<br>
      Central, Hong Kong
    </address>
  </section>

  <section class="card card-back" aria-label="Card back">
    <div class="wordmark">KDT LAND</div>
    <p class="tagline">LIFESTYLE PROPERTY<br>DEVELOPMENT</p>
  </section>
</main>
</body>
</html>
```